Business Card Design

I am a medical doctor who is also trained in eastern medicine and acupuncture. I would like to incorporate the chinese characters for "Balance" in a vertical configuration, prominently featured on the left hand side of the card. (see image that I tried to cut and paste together. There is also a horizontal version, but I would like the characters stacked. I included each character separately) I would like the chinese characters and my name to be in blue or teal with the other print either brown or black. I would like this tag line on the back of the card: "Balancing Western and Eastern Medicine to Achieve Optimal Health". I tried out a similar design in Cardquill Templates but the chinese characters said "sushi". Not exactly appropriate. Many thanks.

Industry/Entity Type

Medical

Contact Information for Business Card

Margaret Delane, MD, LAc
582-B Pohaku St
Kailua, HI 96734
(808) 471-2096
margaretMDneedlework@mailbrook.example
www.margaretMDneedlework.example

```html
<!DOCTYPE html>
<html lang="en">
<head>
<meta charset="utf-8">
<title>Margaret Delane, MD, LAc — Business Card</title>
<link rel="stylesheet" href="https://fonts.googleapis.com/css2?family=Montserrat:wght@700&family=Source+Sans+3:wght@400&display=swap">
<style>
  :root {
    --stage: #ece9e4;
    --card-white: #ffffff;
    --brand-blue: #1782b3;
    --ink-gray: #8b8b8b;
    --on-blue: #ffffff;
    --shadow: 0 3px 8px rgba(0,0,0,0.28);
  }
  * { margin: 0; padding: 0; box-sizing: border-box; }
  html, body {
    width: 1200px; height: 1000px; overflow: hidden;
    background: var(--stage);
  }
  .card {
    position: absolute;
    left: 265px; width: 666px; height: 397px;
    box-shadow: var(--shadow);
  }
  .card--front { top: 73px; background: var(--card-white); }
  .card--back { top: 533px; background: var(--brand-blue); }

  .wordmark {
    font-family: "Montserrat", "Century Gothic", sans-serif;
    font-weight: 700;
    line-height: 1;
    text-transform: uppercase;
  }
  .wordmark--stacked {
    position: absolute; left: 100px; top: 150px;
    font-size: 40px; color: var(--brand-blue);
    display: flex; flex-direction: column; gap: 16px;
    letter-spacing: 2px;
  }
  .wordmark--row {
    position: absolute; left: 0; right: 0; top: 130px;
    text-align: center; font-size: 64px; color: var(--on-blue);
    letter-spacing: 4px;
  }

  .identity { position: absolute; left: 333px; top: 134px; }
  .identity__name {
    font-family: "Montserrat", "Century Gothic", sans-serif;
    font-weight: 700; font-size: 17.5px; color: var(--brand-blue);
  }
  .identity__creds {
    font-family: "Source Sans 3", "Myriad Pro", sans-serif;
    font-weight: 400; font-size: 17.5px; color: var(--brand-blue);
  }
  .contact {
    position: absolute; left: 333px; top: 196px;
    list-style: none;
    font-family: "Source Sans 3", "Myriad Pro", sans-serif;
    font-size: 15.5px; color: var(--ink-gray); line-height: 21px;
  }
  .contact__item { display: flex; align-items: center; gap: 5px; white-space: nowrap; }
  .contact__icon { width: 12px; height: 12px; flex: none; fill: var(--brand-blue); }

  .tagline {
    position: absolute; left: 0; right: 0; top: 296px;
    text-align: center;
    font-family: "Source Sans 3", "Myriad Pro", sans-serif;
    font-size: 18px; color: var(--on-blue);
  }
</style>
</head>
<body>
  <section class="card card--front" aria-label="Business card front">
    <div class="wordmark wordmark--stacked"><span>Still</span><span>Point</span></div>
    <p class="identity"><span class="identity__name">Margaret Delane</span><span class="identity__creds">, MD, LAc</span></p>
    <ul class="contact">
      <li class="contact__item">
        <svg class="contact__icon" viewBox="0 0 12 12" aria-hidden="true"><path d="M3 1.2 4.6 3.4 3.6 4.6C4.3 6.2 5.6 7.6 7.3 8.4L8.5 7.4 10.8 9 10 10.6C9.5 11.2 8.6 11.2 7.6 10.8 4.6 9.4 2.5 7.2 1.3 4.3 1 3.3 1.1 2.4 1.6 2Z"/></svg>
        (808) 471-2096
      </li>
      <li class="contact__item">
        <svg class="contact__icon" viewBox="0 0 12 12" aria-hidden="true"><path d="M0.5 2.5h11v7h-11z"/><path d="M0.8 2.8 6 6.8 11.2 2.8" fill="none" stroke="#fff" stroke-width="1"/></svg>
        margaretMDneedlework@mailbrook.example
      </li>
      <li class="contact__item">
        <svg class="contact__icon" viewBox="0 0 12 12" aria-hidden="true"><circle cx="6" cy="6" r="5.5"/><g fill="none" stroke="#fff" stroke-width="0.8"><ellipse cx="6" cy="6" rx="2.2" ry="5.3"/><path d="M0.6 6h10.8M1.4 3.5h9.2M1.4 8.5h9.2"/></g></svg>
        www.margaretMDneedlework.example
      </li>
    </ul>
  </section>

  <section class="card card--back" aria-label="Business card back">
    <div class="wordmark wordmark--row">Still Point</div>
    <p class="tagline">Balancing Western and Eastern Medicine to Achieve Optimal Health</p>
  </section>
</body>
</html>
```